Wordpress design for lovely french B&B - Mas des Ormeaux

We need a Wordpress design for a B&B located in eastern France.
The current website (designed by the previous owners) is here: http://www.masdesormeaux-exemple.fr. But it's not what we want, it has some photos so you can have a look at what it looks like.
New photos will be taken.

The new design should be fresh, modern and engaging and reflect the fact that it is a lovely B&B with 5 rooms. It is located in a lovely french village, close to the german and swiss border. It is perfectly located, close to the city, stores and highways, and also close to the country side.

The website should be able to describe each of the 5 rooms (1 page per room, with photos, description, price and booking).
The website should also have a pages to display the surrounding activities (one page with country side activities and one page with city activities) and also have a map for directions as well as a contact page with a form.
We will include a wordpress booking plugin so people can book online.

Target Market(s)

People visiting the french country side

Industry/Entity Type

Online

Logo Text

Le Mas des Ormeaux

Font styles to use
Script

Requirements
Must have
• Should feel like it's in the country side, but also feel like it's a little bit of luxury but not too much
Should not have
• I used B&B term to make it understandable, but it should not use the term B&B. It should use the french term "Gîte"

```html
<!DOCTYPE html>
<html lang="fr">
<head>
<meta charset="utf-8">
<title>Le Mas des Ormeaux – Gîte</title>
<link rel="stylesheet" href="https://fonts.googleapis.com/css2?family=Open+Sans:wght@400;600;700&family=Oswald:wght@300;400;500&family=Satisfy&display=swap">
<style>
:root{
  --green:#1d6a37;
  --green-dark:#15502a;
  --green-light:#2f8a4b;
  --charcoal:#2b2b2b;
  --field:#3a3a3a;
  --ink:#333;
  --muted:#777;
  --pale:#efefef;
  --white:#fff;
}
*{box-sizing:border-box;margin:0;padding:0}
html,body{width:828px;height:1200px;overflow:hidden;background:var(--white);font-family:"Open Sans",sans-serif;color:var(--ink)}
.page{width:828px;height:1200px;position:relative;overflow:hidden}

.topbar{height:50px;background:var(--green);display:flex;align-items:center;justify-content:space-between;padding:0 40px 0 110px}
.brand{font-family:"Satisfy",cursive;color:var(--white);font-size:24px}
.contact{display:flex;align-items:center;gap:14px;color:var(--white);font-size:9px;line-height:1.3}
.phone-btn{background:var(--white);color:var(--green);font-weight:700;font-size:10px;padding:6px 10px}
.phone-ico{width:22px;height:22px;border-radius:50%;background:var(--white);display:flex;align-items:center;justify-content:center}

.nav{height:25px;display:flex;justify-content:center;gap:0;border-bottom:1px solid #ddd}
.nav a{font-size:8px;text-decoration:none;color:var(--ink);padding:8px 30px;text-transform:uppercase;letter-spacing:.5px}
.nav a.active{background:var(--green);color:var(--white)}

.booking{height:187px;background:var(--charcoal);color:var(--white);padding-top:14px}
.booking h2{text-align:center;font-family:"Oswald",sans-serif;font-weight:400;font-size:17px;margin-bottom:14px}
.row{display:flex;align-items:center;margin:0 0 8px 120px;font-size:9px}
.row label{width:110px}
.field{width:80px;height:14px;background:var(--field);margin-right:6px}
.field.wide{width:96px}
.cal{width:14px;height:14px;background:#b9c7bd;margin-right:14px}
.book-btn{display:block;margin:14px auto 0;width:170px;background:var(--green);color:var(--white);font-size:8px;text-align:center;padding:7px 0;text-transform:uppercase}

.hero{height:283px;position:relative}
.hero-photo{position:absolute;inset:0;background:linear-gradient(180deg,#a9c3d8 0%,#c9b8a4 45%,#6f5a45 80%,#4d5a3a 100%)}
.hero-text{position:absolute;left:45px;top:72px;color:var(--white);background:rgba(0,0,0,.28);padding:8px 14px}
.hero-text .kicker{font-family:"Oswald",sans-serif;font-weight:300;font-size:26px}
.hero-text .headline{font-family:"Oswald",sans-serif;font-weight:500;font-size:28px;letter-spacing:.5px}
.hero-text .script{font-family:"Satisfy",cursive;font-size:17px}
.hero-card{position:absolute;left:410px;top:30px;width:360px;height:200px;background:var(--white);padding:16px 20px;font-size:8px;line-height:1.5}
.hero-card h3{font-size:13px;margin-bottom:8px}
.more{display:inline-block;margin-top:10px;font-weight:700;font-size:8px}

.gallery{padding-top:22px}
.gallery h2{text-align:center;font-family:"Oswald",sans-serif;font-weight:400;color:var(--green);font-size:30px;margin-bottom:14px}
.item{display:flex;height:98px;margin:0 auto 10px;width:700px;align-items:stretch}
.tag{width:120px;background:var(--pale);display:flex;flex-direction:column;align-items:center;justify-content:center;font-size:9px;color:var(--muted)}
.tag b{font-weight:400;color:var(--ink)}
.thumb{width:200px;margin:0 18px}
.t1{background:linear-gradient(135deg,#7b5c42,#b89a78)}
.t2{background:linear-gradient(135deg,#5f7d4b,#a8b58e)}
.t3{background:linear-gradient(135deg,#6a4a35,#c6a98a)}
.t4{background:linear-gradient(135deg,#8a6c52,#d8c4a8)}
.desc{flex:1;font-size:7.5px;line-height:1.5;padding-top:6px}
.desc h3{font-size:12px;margin-bottom:4px}

.cta{position:absolute;top:1060px;left:0;width:828px;height:52px;background:var(--green-dark);display:flex;align-items:center;padding-left:115px}
.cta span{background:var(--white);color:var(--green);font-size:8px;font-weight:700;padding:7px 36px;text-transform:uppercase}

.footer{position:absolute;top:1112px;left:0;width:828px;height:60px;background:var(--pale);display:flex;padding:8px 0 0 115px;gap:0;font-size:7px}
.col{width:210px}
.col h4{font-size:9px;font-weight:600;margin-bottom:4px}
.links{display:grid;grid-template-columns:60px 60px;gap:2px;color:var(--muted)}
.social{display:flex;gap:6px}
.social i{width:14px;height:14px;border-radius:50%;background:#999;display:block}
.news{display:flex;margin-top:4px}
.news span{width:90px;height:12px;background:var(--white)}
.news b{background:var(--green);color:var(--white);font-size:6px;padding:2px 6px}

.bottombar{position:absolute;top:1172px;left:0;width:828px;height:28px;background:var(--green);display:flex;align-items:center;justify-content:space-between;padding:0 80px 0 115px;color:var(--white);font-size:7px}
.bottombar .brand{font-size:15px}
</style>
</head>
<body>
<div class="page">
  <header class="topbar">
    <div class="brand">Le Mas des Ormeaux</div>
    <div class="contact">
      <div>Email: contact@masdesormeaux-exemple.fr<br>Phone Number</div>
      <div class="phone-btn">+33 (0)3 00 00 00 00</div>
      <div class="phone-ico"><svg width="12" height="12" viewBox="0 0 24 24"><path fill="#1d6a37" d="M6.6 10.8a15 15 0 0 0 6.6 6.6l2.2-2.2c.3-.3.7-.4 1-.2 1.1.4 2.3.6 3.6.6.6 0 1 .4 1 1V20c0 .6-.4 1-1 1A17 17 0 0 1 3 4c0-.6.4-1 1-1h3.5c.6 0 1 .4 1 1 0 1.3.2 2.5.6 3.6.1.3 0 .7-.2 1z"/></svg></div>
    </div>
  </header>
  <nav class="nav">
    <a href="#">Home</a><a href="#" class="active">Pages</a><a href="#">Price</a><a href="#">Country Side</a><a href="#">City Side</a><a href="#">Contact Us</a>
  </nav>

  <section class="booking">
    <h2>Room Reservations</h2>
    <div class="row"><label>Arrival Date:</label><span class="field"></span><span class="field"></span><span class="field wide"></span><span class="cal"></span><span class="field"></span></div>
    <div class="row"><label>Departure Date:</label><span class="field"></span><span class="field"></span><span class="field wide"></span><span class="cal"></span><span class="field"></span></div>
    <div class="row"><label>Number Nights:</label><span>1 Night</span></div>
    <span class="book-btn">Check Availability &amp; Book Now</span>
  </section>

  <section class="hero">
    <div class="hero-photo" role="img" aria-label="Photo of half-timbered village houses in Alsace under a blue sky"></div>
    <div class="hero-text">
      <div class="kicker">Explore Our Region</div>
      <div class="headline">LONG STAYS IN ALSACE</div>
      <div class="script">satisfy you throughout your stay</div>
    </div>
    <div class="hero-card">
      <h3>Title is here</h3>
      <p>The gîte is ideally set in a quiet Alsace village, close to the city, shops and motorways as well as the countryside. Each of our five rooms offers a calm and comfortable stay.</p>
      <p>– Village walks, vineyards, markets and local festivals nearby</p>
      <p>– Germany and Switzerland only a short drive away</p>
      <span class="more">click to see more</span>
    </div>
  </section>

  <section class="gallery">
    <h2>Photo Gallery</h2>
    <div class="item"><div class="tag"><b>Le Mas des</b>Ormeaux</div><div class="thumb t1" role="img" aria-label="Photo of a guest room"></div><div class="desc"><h3>Title is here</h3><p>The gîte is set in a quiet village with easy access to city and countryside. Bright rooms with a private bath.</p><p>– Village walks, vineyards and local dining.</p><b>click to see more</b></div></div>
    <div class="item"><div class="tag"><b>Le Mas des</b>Ormeaux</div><div class="thumb t2" role="img" aria-label="Photo of the garden terrace"></div><div class="desc"><h3>Title is here</h3><p>The gîte is set in a quiet village with easy access to city and countryside. Shaded terrace for breakfast.</p><p>– Village walks, vineyards and local dining.</p><b>click to see more</b></div></div>
    <div class="item"><div class="tag"><b>Le Mas des</b>Ormeaux</div><div class="thumb t3" role="img" aria-label="Photo of the dining room"></div><div class="desc"><h3>Title is here</h3><p>The gîte is set in a quiet village with easy access to city and countryside. Homemade regional breakfast.</p><p>– Village walks, vineyards and local dining.</p><b>click to see more</b></div></div>
    <div class="item"><div class="tag"><b>Le Mas des</b>Ormeaux</div><div class="thumb t4" role="img" aria-label="Photo of a bedroom with timber beams"></div><div class="desc"><h3>Title is here</h3><p>The gîte is set in a quiet village with easy access to city and countryside. Cosy beds under old beams.</p><p>– Village walks, vineyards and local dining.</p><b>click to see more</b></div></div>
  </section>

  <div class="cta"><span>Click Here</span></div>

  <footer class="footer">
    <div class="col"><h4>Other Links</h4><div class="links"><span>› Rooms</span><span>› Country Side</span><span>› Prices</span><span>› City Side</span><span>› Booking</span><span>› Contact</span></div></div>
    <div class="col"><h4>Visit our Social Media</h4><div class="social"><i></i><i></i><i></i><i></i></div></div>
    <div class="col"><h4>Newsletter</h4><p>Sign up for news and seasonal offers.</p><div class="news"><span></span><b>SUBSCRIBE</b></div></div>
  </footer>
  <div class="bottombar"><span class="brand">Le Mas des Ormeaux</span><span>Copyright © 2015 · masdesormeaux · All Rights Reserved</span><span>BACK TO TOP</span></div>
</div>
</body>
</html>
```